Brom Vela CEO and Partners Business Card

We need a fresh, fun, simple and clean business card design....we would like a template where we can add a name and title (as well as specific email addresses). We are open to different looks (full logo on one side and a small logo on the company info side, or our logo is in the background but faint on one side but full on the other, or something else cool :-) ). Our colors are in our logo: blue, black and white...however we are not opposed to the use of other colors if it works. We build sets, make props and a host of other things for the film and television industry...our card should reflect creativity, style and professionalism.

A white background would be preferred.

I would like to see an option with Facebook and Instagram icons.

Facebook- facebook.com/bromvelaqt
Instagram- brom_vela

Our website is bromvela-example.com.

Brom Vela, Inc.
4168 Tolliver Crescent, Unit 9
Ferris Hollow, Lennox Vale 40813
555.210.4872 | tel
555.210.6391 | fax
www.BromVela-example.com

Sample Name and Title #1:

Curtis Welbore
CEO / Co-Owner
555.210.4872 | tel
555.210.6391 | fax
curtis@bromvela-example.com
www.BromVela-example.com

Target Market(s)

Marketing Professionals, Production Designers, Interior Designers, Film Producers, Directors, Art Directors, Event Directors

Industry/Entity Type

Entertainment Industry

Contact Information for Business Card

Curtis Welbore
CEO / Co-Owner
555.210.4872 | tel
555.210.6391 | fax
curtis@bromvela-example.com
www.BromVela-example.com

Font styles to use
Sans Serif

Colors
33a6d7
ffffff
1b1b1b

Requirements
Must have
• Logo, All Contact Info, White Background. Symmetry.
Nice to have
• Facebook and Instagram icons with addresses
• Facebook- facebook.com/bromvelaqt
• Instagram- brom_vela

```html
<!DOCTYPE html>
<html lang="en">
<head>
<meta charset="utf-8">
<title>Brom Vela CEO and Partners Business Card</title>
<link href="https://fonts.googleapis.com/css2?family=Source+Sans+3:wght@400;600;800&display=swap" rel="stylesheet">
<style>
  :root {
    --blue: #33a6d7;
    --ink: #1b1b1b;
    --white: #ffffff;
    --grey-text: #4a4a4a;
    --rule: #d4d4d4;
    --stage: #ececec;
  }
  * { margin: 0; padding: 0; box-sizing: border-box; }
  html, body {
    width: 1200px; height: 987px; overflow: hidden;
    background: var(--stage);
    font-family: "Source Sans 3", "Helvetica Neue", Arial, sans-serif;
  }
  .card {
    position: absolute;
    left: 293px; width: 615px; height: 350px;
    box-shadow: 0 2px 6px rgba(0,0,0,.18);
  }
  .card--front { top: 130px; background: var(--white); }
  .card--back  { top: 506px; background: #000; }

  .wordmark {
    position: absolute;
    font-weight: 800;
    letter-spacing: -0.5px;
    white-space: nowrap;
    text-transform: uppercase;
    transform: translate(-50%, -50%);
  }
  .card--front .wordmark { left: 176px; top: 190px; font-size: 40px; color: var(--ink); }
  .card--back .wordmark { left: 308px; top: 175px; font-size: 74px; color: var(--white); }

  .divider {
    position: absolute; left: 322px; top: 69px;
    width: 1px; height: 246px; background: var(--rule);
  }
  .contact { position: absolute; left: 349px; top: 75px; color: var(--grey-text); }
  .contact__name { font-size: 22px; font-weight: 600; color: var(--blue); line-height: 28px; }
  .contact__title { font-size: 16px; color: var(--ink); line-height: 20px; margin-left: 2px; }
  .contact__address { font-size: 15.5px; line-height: 21.5px; margin-top: 14px; margin-left: 2px; }
  .contact__lines { list-style: none; margin-top: 13px; margin-left: 2px; font-size: 15.5px; }
  .contact__lines li { display: flex; align-items: center; height: 23.5px; }
  .contact__lines svg { width: 14px; height: 14px; margin-right: 8px; fill: var(--blue); flex: none; }

  .social {
    position: absolute; left: 0; right: 0; top: 290px;
    display: flex; justify-content: center; gap: 14px;
    color: var(--white); font-size: 17px;
  }
  .social__item { display: flex; align-items: center; }
  .social__mark { width: 17px; height: 17px; background: var(--blue); margin-right: 4px; }
</style>
</head>
<body>
  <section class="card card--front" aria-label="Business card front">
    <div class="wordmark">Brom Vela</div>
    <div class="divider"></div>
    <div class="contact">
      <p class="contact__name">Curtis Welbore</p>
      <p class="contact__title">CEO / Co-Owner</p>
      <p class="contact__address">4168 Tolliver Crescent<br>Unit 9, Ferris Hollow<br>Lennox Vale 40813</p>
      <ul class="contact__lines">
        <li><svg viewBox="0 0 16 16" aria-hidden="true"><path d="M3.6 1.2l2.3 2.6c.4.4.3 1-.1 1.4L4.6 6.3c.9 2 2.6 3.8 4.9 5l1.1-1.2c.4-.4 1-.4 1.4-.1l2.6 2.1c.4.3.4.9.1 1.3l-1.2 1.4c-.5.5-1.3.7-2 .4C6.3 13.4 2.7 9.8 1 4.6c-.2-.7 0-1.4.5-1.9l1.2-1.3c.3-.4.7-.4.9-.2z"/></svg>555.210.4872</li>
        <li><svg viewBox="0 0 16 16" aria-hidden="true"><rect x="4" y="1" width="8" height="5"/><rect x="1" y="7" width="14" height="5" rx="1"/><rect x="3" y="12.5" width="10" height="2.5"/></svg>555.210.6391</li>
        <li><svg viewBox="0 0 16 16" aria-hidden="true"><path d="M1 3.5h14v9H1z" opacity=".9"/><path d="M1 3.5l7 5 7-5" fill="none" stroke="#fff" stroke-width="1.2"/></svg>curtis@bromvela-example.com</li>
        <li><svg viewBox="0 0 16 16" aria-hidden="true"><circle cx="8" cy="8" r="7"/><path d="M1 8h14M8 1c2.5 2.5 2.5 11.5 0 14M8 1c-2.5 2.5-2.5 11.5 0 14" fill="none" stroke="#fff" stroke-width="1"/></svg>www.BromVela-example.com</li>
      </ul>
    </div>
  </section>

  <section class="card card--back" aria-label="Business card back">
    <div class="wordmark">Brom Vela</div>
    <div class="social">
      <span class="social__item"><span class="social__mark"></span>bromvelaqt</span>
      <span class="social__item"><span class="social__mark"></span>brom_vela</span>
    </div>
  </section>
</body>
</html>
```